Flaschenetikett Jörgi`s ColaMix
Zielgruppe
Wir machen einen ColaMix, weil wir es können und ihm eine Prise 80er verpassen wollen.
Hip, Trendig und ein bisschen Oldschool.
Bei uns kommt nur in die Flasche, was uns selber schmeckt und dabei preislich fair ist! Kein Schnickschnack, dafür mit viel Geschmack und einer Portion Oldschool.
Einfach einen richtig guten Brauso ähhmm, ColaMix!
Farben:
orange / weiss (Hintergrund Orange & Schrift Weiss)
oder
weiss / anthrazit
Flaschenfarbe:
braun
Etikettgröße:
max. 10 x 10 cm
Name:
Jörgis ColaMix
Zusatztext:
MÜNCHEN
ColaMix (muss irgendwo auf dem Etikett stehen)
Die Beispiele finden wir ultra hip, ein bisschen oldschool, trendig und genau richtig. Alles simpel, kein BlimBlim aber dafür einen ziemlich hohen Stylfaktor.
Wir sind nicht modern, sondern Kinder der 80iger, stehen auf Industrie Vintage Zeug und brauchen einen "ColaMix" der zu uns passt.
Jörg, ja einfach Jörg soll er heissen. Ein deutscher Trendname aus dem 19.Jahrhundert und doch jung und frisch! Genau wie unser ColaMix.
Das Kultgetränk das Allen schmeckt kommt in einer Oldschool braunen Flasche um die Ecke.
WIR MACHEN UNS FAST IN DIE HOSEN VOR AUFREGUNG, WAS IHR SO AUF DER FLASCHE HABT!!!!
HAUT REIN!!!

```html
<!DOCTYPE html>
<html lang="de">
<head>
<meta charset="utf-8">
<title>Jörgs ColaMix – Flaschenetikett</title>
<link rel="stylesheet" href="https://fonts.googleapis.com/css2?family=Oswald:wght@400;500;600&family=Open+Sans:wght@600;700&display=swap">
<style>
  :root {
    --orange: #f47e20;
    --orange-light: #f5a865;
    --anthracite: #58585a;
    --white: #ffffff;
    --page: #ffffff;
  }
  html, body {
    margin: 0;
    padding: 0;
    width: 1200px;
    height: 900px;
    overflow: hidden;
    background: var(--page);
  }
  .canvas {
    position: relative;
    width: 1200px;
    height: 900px;
  }
  .label {
    position: absolute;
    left: 341px;
    top: 173px;
    width: 517px;
    height: 517px;
    background: var(--orange);
    overflow: hidden;
  }
  .frame-outer {
    position: absolute;
    inset: 9px;
    border: 3px solid var(--white);
  }
  .frame-inner {
    position: absolute;
    inset: 17px;
    border: 1.5px solid var(--white);
  }
  .sunburst {
    position: absolute;
    left: 48px;
    top: 50px;
    width: 420px;
    height: 420px;
    border-radius: 50%;
    background: radial-gradient(circle, var(--orange-light) 0%, rgba(245,168,101,0.75) 40%, rgba(245,168,101,0) 70%);
  }
  .tab {
    position: absolute;
    left: 230px;
    top: 0;
    width: 56px;
    height: 73px;
    background: var(--anthracite);
    border-radius: 0 0 28px 28px;
    box-shadow: 0 0 0 3px var(--orange);
  }
  .tab-mark {
    position: absolute;
    left: 9px;
    bottom: 9px;
    width: 34px;
    height: 34px;
    border: 2px solid var(--white);
    border-radius: 50%;
  }
  .since {
    position: absolute;
    top: 37px;
    font-family: "Open Sans", sans-serif;
    font-weight: 700;
    font-size: 15px;
    letter-spacing: 2px;
    color: var(--anthracite);
  }
  .since-word { left: 163px; transform: rotate(-14deg); }
  .since-year { left: 297px; transform: rotate(14deg); }
  .brand {
    position: absolute;
    left: 190px;
    top: 107px;
    width: 136px;
    height: 62px;
    border-top: 3px solid var(--white);
    border-bottom: 3px solid var(--white);
    text-align: center;
    font-family: "Oswald", sans-serif;
    font-weight: 500;
    font-size: 52px;
    line-height: 62px;
    color: var(--white);
    letter-spacing: 1px;
  }
  .product {
    position: absolute;
    left: 0;
    width: 517px;
    top: 178px;
    text-align: center;
    font-family: "Oswald", sans-serif;
    font-weight: 600;
    font-size: 128px;
    line-height: 150px;
    color: var(--white);
  }
  .ribbon {
    position: absolute;
    left: 95px;
    top: 428px;
    width: 313px;
    height: 52px;
  }
  .ribbon-text {
    position: absolute;
    left: 137px;
    top: 428px;
    width: 243px;
    height: 40px;
    text-align: center;
    font-family: "Oswald", sans-serif;
    font-weight: 500;
    font-size: 17px;
    line-height: 40px;
    letter-spacing: 2.5px;
    color: var(--white);
  }
  .volume {
    position: absolute;
    left: 14px;
    top: 444px;
    transform: rotate(-90deg);
    transform-origin: center;
    font-family: "Oswald", sans-serif;
    font-weight: 500;
    font-size: 17px;
    color: var(--white);
    letter-spacing: 1px;
  }
  .legal {
    position: absolute;
    left: 340px;
    top: 397px;
    width: 180px;
    transform: rotate(-90deg);
    font-family: "Open Sans", sans-serif;
    font-weight: 600;
    font-size: 8.5px;
    color: var(--white);
    white-space: nowrap;
  }
</style>
</head>
<body>
<main class="canvas">
  <section class="label">
    <div class="sunburst" role="img" aria-label="Strahlenkranz in hellem Orange hinter dem Schriftzug"></div>
    <div class="frame-outer"></div>
    <div class="frame-inner"></div>

    <div class="tab"><div class="tab-mark"></div></div>
    <span class="since since-word">SINCE</span>
    <span class="since since-year">2016</span>

    <div class="brand">JÖRGS</div>
    <div class="product">ColaMix</div>

    <svg class="ribbon" viewBox="0 0 313 52" aria-hidden="true">
      <polygon points="0,10 42,10 42,52 0,52 12,31" fill="var(--anthracite)"/>
      <polygon points="313,10 271,10 271,52 313,52 301,31" fill="var(--anthracite)"/>
      <polygon points="42,40 42,52 30,40" fill="#3f3f41"/>
      <polygon points="271,40 271,52 283,40" fill="#3f3f41"/>
      <rect x="42" y="0" width="229" height="40" fill="var(--anthracite)" stroke="var(--white)" stroke-width="2"/>
    </svg>
    <div class="ribbon-text">MADE FOR MUNICH</div>

    <div class="volume">0,5 L</div>
    <div class="legal">COFFEINHALTIGES MIXGETRÄNK</div>
  </section>
</main>
</body>
</html>
```